Land Buying Company Needs Letterhead for Direct Mail Marketing to Land Owners

We are looking for a professional letterhead that we will be including in our direct mail marketing. We will be sending this to land owners who may be interested in selling or purchasing land.

The letterhead needs to be editable. Headers and footers would look nice, but we are open. We would want it to include our address, website, phone, and email info. For right now the address to use for design purposes would the following:

Address: 412 Fenwick Avenue #300
Dallas, TX 75319
Website - www.quillbrookacres.com
Email - info@quillbrookacres.com
Phone - 866-492-ACRE

I have attached our logo zip file that we just had done on Pixel Harbor. Let me know what questions you have, and thank you.

```html
<!DOCTYPE html>
<html lang="en">
<head>
<meta charset="utf-8">
<title>Quillbrook Acres Letterhead</title>
<link rel="stylesheet" href="https://fonts.googleapis.com/css2?family=Lato:wght@400&family=Montserrat:wght@400;700&display=swap">
<style>
  :root {
    --backdrop: #d6d6d6;
    --paper: #ffffff;
    --forest: #3f5a29;
    --leaf: #8cc63f;
    --body-text: #555555;
  }
  * { margin: 0; padding: 0; box-sizing: border-box; }
  html, body { width: 1056px; height: 1200px; overflow: hidden; background: var(--backdrop); }
  .letterhead {
    position: absolute; left: 104px; top: 0;
    width: 848px; height: 1200px;
    background: var(--paper);
    font-family: "Lato", sans-serif;
    color: var(--body-text);
  }
  .brand {
    position: absolute; left: 77px; top: 76px;
    display: flex; align-items: center; gap: 18px;
  }
  .brand-dot { width: 73px; height: 73px; border-radius: 50%; background: var(--forest); }
  .brand-name {
    font-family: "Montserrat", sans-serif; font-weight: 700;
    font-size: 30px; letter-spacing: 1px; color: var(--leaf);
    text-transform: uppercase;
  }
  .letter-body {
    position: absolute; left: 77px; top: 280px; width: 689px;
    font-size: 15.5px; line-height: 29.5px; text-align: justify;
  }
  .letter-body p { margin-bottom: 29.5px; }
  .salutation { margin-bottom: 26px !important; }
  .closing { position: absolute; left: 77px; top: 884px; font-size: 15.5px; }
  .signature {
    position: absolute; left: 74px; top: 920px; width: 68px; height: 44px;
    background: linear-gradient(90deg, rgba(63,90,41,0.25), rgba(63,90,41,0.08));
    border-radius: 4px;
  }
  .contact {
    position: absolute; left: 74px; top: 1040px;
    font-family: "Montserrat", sans-serif; font-size: 12.5px; color: var(--forest);
  }
  .contact-address { line-height: 17px; margin-bottom: 8px; }
  .contact-line { display: flex; align-items: center; height: 19.5px; }
  .contact-line svg { width: 13px; height: 13px; margin-right: 16px; }
  .footer-band { position: absolute; left: 0; bottom: 0; width: 848px; height: 18px; }
</style>
</head>
<body>
  <main class="letterhead">
    <header class="brand">
      <div class="brand-dot"></div>
      <div class="brand-name">Quillbrook Acres</div>
    </header>

    <section class="letter-body">
      <p class="salutation">Dear Sir/Mam,</p>
      <p>Contrary to popular belief, Lorem Ipsum is not simply random text. It has roots in a piece of classical Latin literature from 45 BC, making it over 2000 years old. Daniel Hartwell, a Latin professor at Ashgrove College in Virginia, looked up one of the more obscure Latin words, consectetur.</p>
      <p>Lorem Ipsum comes from sections 1.10.32 and 1.10.33 of "de Finibus Bonorum et Malorum" (The Extremes of Good and Evil) by Lucius Vetrano, written in 45 BC. This book is a treatise on the theory of ethics, very popular during the Renaissance. The first line of Lorem Ipsum.</p>
      <p>The standard chunk of Lorem Ipsum used since the 1500s is reproduced below for those interested. Sections 1.10.32 and 1.10.33 from "de Finibus Bonorum et Malorum" by Lucius Vetrano are also reproduced in their exact original.</p>
      <p>The standard chunk of Lorem Ipsum used since the 1500s is reproduced below for those interested.</p>
    </section>

    <p class="closing">Best Regards</p>
    <div class="signature" role="img" aria-label="Handwritten signature"></div>

    <footer class="contact">
      <div class="contact-address">412 Fenwick Avenue #300<br>Dallas, TX 75319</div>
      <div class="contact-line">
        <svg viewBox="0 0 16 16" aria-hidden="true"><path fill="#8cc63f" d="M3.5 1.5l2.5 0 1 3.5-1.6 1.2a9 9 0 0 0 4.4 4.4L11 9l3.5 1v2.5c0 1-.8 1.8-1.8 1.8C7 14.3 1.7 9 1.7 3.3c0-1 .8-1.8 1.8-1.8z"/></svg>
        866-492-ACRE
      </div>
      <div class="contact-line">
        <svg viewBox="0 0 16 16" aria-hidden="true"><rect x="1" y="3" width="14" height="10" fill="#8cc63f"/><path d="M1 3l7 5.5L15 3" fill="none" stroke="#fff" stroke-width="1.3"/></svg>
        info@quillbrookacres.com
      </div>
      <div class="contact-line">
        <svg viewBox="0 0 16 16" aria-hidden="true"><g fill="none" stroke="#8cc63f" stroke-width="1.2"><circle cx="8" cy="8" r="6.5"/><ellipse cx="8" cy="8" rx="3" ry="6.5"/><path d="M1.5 8h13M2.6 4.8h10.8M2.6 11.2h10.8"/></g></svg>
        www.quillbrookacres.com
      </div>
    </footer>

    <svg class="footer-band" viewBox="0 0 848 18" preserveAspectRatio="none" aria-hidden="true">
      <polygon points="0,0 427,0 419,18 0,18" fill="var(--forest)"/>
      <polygon points="440,0 848,0 848,18 432,18" fill="var(--leaf)"/>
    </svg>
  </main>
</body>
</html>
```